Meridane Haulage - Website

A clean, not cluttered informative website for our business. We specialize in the transportation of radioactive materials across North America. The site is mostly for information about our company and will not be used to attract business but will be used to attract employee's mainly drivers. Driver's are very hard to find in our area. One of the pages needs to be a job's posting page with an apply now button. Either an application can be filled out there or a resume can be uploaded which ever functionality works better. I would like a website that I can easily edit, ability to change text and photos.

Number of Pages Required

5+ page

Colors

Designer to choose colors to be used in the design.

Requirements
Must have
• Home - About - Services - Jobs - Contact pages
• A way prospective employee's can apply or upload their resume to be emailed to me
• Very clean apperance
Should not have
• I don't want it to be busy

```html
<!DOCTYPE html>
<html lang="en">
<head>
<meta charset="utf-8">
<title>Meridane Haulage</title>
<link href="https://fonts.googleapis.com/css2?family=Roboto:wght@400;500;700&family=Open+Sans:wght@400;600&display=swap" rel="stylesheet">
<style>
:root{
  --blue:#1673c4;
  --blue-dark:#0f5fa6;
  --ink:#333;
  --white:#fff;
  --dark:#2b2c2e;
}
*{box-sizing:border-box;margin:0;padding:0}
html,body{width:1200px;height:3285px;overflow:hidden}
body{position:relative;background:var(--white);font-family:"Open Sans",sans-serif;color:var(--ink)}
.abs{position:absolute}
.topbar{left:0;top:0;width:1200px;height:61px;background:var(--blue);color:var(--white)}
.topbar .phone{left:90px;top:18px;font-size:15px;display:flex;align-items:center;gap:24px}
.social{display:flex;gap:8px}
.social span{width:22px;height:22px;background:var(--white);border-radius:3px;display:block}
.topbar .social{right:90px;top:20px}
.hero{left:0;top:61px;width:1200px;height:620px;background:linear-gradient(180deg,#4c4f53 0%,#5d6166 45%,#3f4245 100%)}
.brand{font-family:"Roboto",sans-serif;font-weight:700;letter-spacing:1px;display:flex;align-items:center;gap:14px}
.brand i{display:block;border-radius:50%}
.hero .brand{left:92px;top:120px;font-size:44px;color:var(--blue)}
.hero .brand i{width:28px;height:28px;background:var(--blue)}
.nav{top:126px;left:770px;display:flex;gap:22px;font-family:"Roboto",sans-serif;font-weight:500;font-size:15px;color:var(--white)}
.nav .active{color:var(--blue)}
.hero h1{left:0;width:1200px;top:296px;text-align:center;font-family:"Roboto",sans-serif;font-weight:700;font-size:54px;color:var(--white)}
.hero .lede{left:0;width:1200px;top:374px;text-align:center;font-size:24px;color:var(--white)}
.btn{display:flex;align-items:center;justify-content:center;border-radius:6px;font-family:"Roboto",sans-serif;font-size:18px}
.btn-ghost{border:2px solid var(--white);color:var(--white)}
.btn-line{border:2px solid var(--blue);color:var(--blue)}
.hero .btn{left:501px;top:447px;width:244px;height:59px;border-color:var(--blue);font-size:22px}
.wave{left:0;width:1200px}
h2{font-family:"Roboto",sans-serif;font-weight:500}
.about h2{left:92px;top:812px;font-size:40px;color:var(--blue)}
.body-text{font-size:20px;line-height:32px}
.about p{left:92px;top:912px;width:480px}
.photo-circle{border-radius:50%;border:13px solid var(--blue)}
.about .photo-circle{left:661px;top:744px;width:430px;height:430px;background:linear-gradient(135deg,#cfd6dc,#7f8a70 55%,#a8b2bb)}
.about .btn{left:92px;top:1117px;width:160px;height:48px}
.services{left:0;top:1259px;width:1200px;height:526px;background:linear-gradient(180deg,#3b3c3e,#242526)}
.services h2{left:0;width:1200px;top:1352px;text-align:center;font-size:44px;color:var(--white)}
.services p{left:120px;width:960px;text-align:center;font-size:18px;line-height:25px;color:var(--white)}
.services .btn{left:521px;top:1621px;width:169px;height:48px}
.jobs .photo-circle{left:123px;top:1853px;width:394px;height:394px;background:linear-gradient(135deg,#7a8fa8,#c9703a 55%,#4c6f9c)}
.jobs h2{left:609px;top:1873px;font-size:42px;color:var(--blue)}
.jobs p{left:609px;top:1958px;width:420px}
.jobs .btn{left:609px;top:2124px;width:173px;height:48px}
.contact{left:0;top:2321px;width:1200px;height:526px;background:linear-gradient(180deg,#45484a,#2c2f30 60%,#3a3d3b)}
.contact h2{left:0;width:1200px;top:2390px;text-align:center;font-size:42px;color:var(--white)}
.field{background:var(--white);font-size:13px;color:#333;padding:10px 20px;font-family:"Roboto",sans-serif}
.contact .btn{left:495px;top:2740px;width:191px;height:48px}
.footer{left:0;top:2847px;width:1200px;height:438px;background:var(--blue);color:var(--white)}
.footer .brand{left:92px;top:2925px;font-size:40px;color:var(--white)}
.footer .brand i{width:24px;height:24px;background:var(--white)}
.footer h3{font-family:"Roboto",sans-serif;font-weight:700;font-size:20px;top:2945px}
.foot-text{font-size:16px;line-height:28px}
.links{list-style:none}
.contact-list div{display:flex;gap:12px;align-items:flex-start}
.footer .copy{left:92px;top:3238px;font-size:15px}
.footer .social{left:966px;top:3239px}
</style>
</head>
<body>
<header class="abs topbar">
  <div class="abs phone">
    <svg width="22" height="22" viewBox="0 0 24 24"><path fill="#fff" d="M6.6 10.8c1.4 2.8 3.8 5.1 6.6 6.6l2.2-2.2c.3-.3.7-.4 1-.2 1.1.4 2.3.6 3.6.6.6 0 1 .4 1 1V20c0 .6-.4 1-1 1C10.6 21 3 13.4 3 4c0-.6.4-1 1-1h3.5c.6 0 1 .4 1 1 0 1.3.2 2.5.6 3.6.1.3 0 .7-.2 1z"/></svg>
    <span>(555) 014-2290.</span>
  </div>
  <div class="abs social"><span></span><span></span><span></span><span></span><span></span></div>
</header>

<section class="abs hero" role="img" aria-label="Photograph of a transport truck hauling cargo beneath bare trees"></section>
<div class="abs brand" style="left:92px;top:120px;font-size:44px;color:var(--blue)"><i style="width:28px;height:28px;background:var(--blue)"></i>MERIDANE HAULAGE</div>
<nav class="abs nav"><span class="active">Home</span><span>About</span><span>Services</span><span>Jobs</span><span>Contact</span></nav>
<h1 class="abs hero-title" style="left:0;width:1200px;top:296px;text-align:center;font-family:'Roboto',sans-serif;font-weight:700;font-size:54px;color:#fff">Welcome to Meridane Haulage</h1>
<p class="abs hero-lede" style="left:0;width:1200px;top:374px;text-align:center;font-size:24px;color:#fff">Currently Hiring&nbsp; Freight Sales&nbsp; AgentsCheck Out&nbsp; Our Employment Area.</p>
<div class="abs btn btn-ghost" style="left:501px;top:447px;width:244px;height:59px;border-color:var(--blue);font-size:22px">View Services</div>
<svg class="abs wave" style="top:610px" width="1200" height="80" viewBox="0 0 1200 80"><path fill="#fff" d="M0 45 C250 5 450 20 650 45 C850 70 1050 60 1200 25 L1200 80 L0 80Z"/></svg>

<section class="about">
  <h2 class="abs">About us Meridane Haulage</h2>
  <p class="abs body-text">Meridane Haulage. has been providing quality transportation services since our founding in 1999.Meridane Haulage. is part of the Meridane Haulage.Group of Companies. Meridane Haulage. is part of the Meridane Haulage&nbsp; of Companies.</p>
  <div class="abs btn btn-line">Read More</div>
  <div class="abs photo-circle" role="img" aria-label="Photograph of a hand holding banknotes in front of parked trucks"></div>
</section>

<section class="abs services" role="img" aria-label="Dark photograph of a truck on the road"></section>
<svg class="abs wave" style="top:1258px" width="1200" height="60" viewBox="0 0 1200 60"><path fill="#fff" d="M0 0 L1200 0 L1200 10 C1000 -5 800 -5 600 20 C400 45 200 30 0 0Z"/></svg>
<h2 class="abs" style="left:0;width:1200px;top:1352px;text-align:center;font-size:44px;color:#fff">Services</h2>
<p class="abs" style="left:120px;width:960px;top:1456px;text-align:center;font-size:18px;line-height:25px;color:#fff">At&nbsp; Meridane Haulage., we specialize in both expedited and regular LTL, Partial Load and Full Truck Load service between Canada, the USA. and Mexico.</p>
<p class="abs" style="left:120px;width:960px;top:1527px;text-align:center;font-size:18px;line-height:25px;color:#fff">In addition, to meet our just in time door to door service requirements, our policy includes one line hauls right to your delivery, which eliminates extra handling of your products which also in turn reduces damages and claims.</p>
<div class="abs btn btn-ghost" style="left:521px;top:1621px;width:169px;height:48px">Read More</div>

<section class="jobs">
  <div class="abs photo-circle" role="img" aria-label="Photograph of a truck driver in a safety vest seated in a cab"></div>
  <h2 class="abs">Jobs</h2>
  <p class="abs body-text">Meridane Haulage is an international carrier which provides service between Canada and the United States with domestic service in each country.</p>
  <div class="abs btn btn-line">Apply Now</div>
</section>

<section class="abs contact" role="img" aria-label="Photograph of a tanker truck on a highway"></section>
<svg class="abs wave" style="top:2320px" width="1200" height="60" viewBox="0 0 1200 60"><path fill="#fff" d="M0 0 L1200 0 L1200 20 C1000 -5 800 -5 600 15 C400 35 200 30 0 0Z"/></svg>
<h2 class="abs" style="left:0;width:1200px;top:2390px;text-align:center;font-size:42px;color:#fff">Contact us</h2>
<div class="abs field" style="left:142px;top:2481px;width:449px;height:37px">Name</div>
<div class="abs field" style="left:609px;top:2481px;width:449px;height:37px">Email</div>
<div class="abs field" style="left:142px;top:2536px;width:449px;height:37px">Phone Number</div>
<div class="abs field" style="left:609px;top:2536px;width:449px;height:37px;display:flex;justify-content:space-between;align-items:center;padding-top:0;padding-bottom:0">Services<svg width="10" height="6" viewBox="0 0 10 6"><path d="M0 0h10L5 6z" fill="#222"/></svg></div>
<div class="abs field" style="left:142px;top:2589px;width:916px;height:111px">Messages</div>
<div class="abs btn btn-ghost" style="left:495px;top:2740px;width:191px;height:48px">Submit</div>

<footer class="abs footer"></footer>
<div class="abs brand" style="left:92px;top:2925px;font-size:40px;color:#fff"><i style="width:24px;height:24px;background:#fff"></i>MERIDANE<br>HAULAGE</div>
<p class="abs foot-text" style="left:92px;top:3018px;width:330px;color:#fff">Meridane Haulage. has been providing quality transportation services since our founding in 1999.</p>
<h3 class="abs" style="left:451px;top:2945px;font-family:'Roboto',sans-serif;font-size:20px;color:#fff">Quick Links</h3>
<ul class="abs links foot-text" style="left:458px;top:3019px;color:#fff"><li>Home</li><li>About</li><li>Services</li><li>Jobs</li><li>Contact</li></ul>
<h3 class="abs" style="left:609px;top:2945px;font-family:'Roboto',sans-serif;font-size:20px;color:#fff">Contact us</h3>
<div class="abs contact-list foot-text" style="left:609px;top:3019px;color:#fff">
  <div><svg width="18" height="24" viewBox="0 0 18 24" style="margin-top:4px"><path fill="#fff" d="M9 0C4 0 0 4 0 9c0 6.5 9 15 9 15s9-8.5 9-15c0-5-4-9-9-9zm0 12.5A3.5 3.5 0 1 1 9 5.5a3.5 3.5 0 0 1 0 7z"/></svg><span>418 Kestrel Road,<br>Toronto, ON<br>M1X 0A0</span></div>
  <div><svg width="18" height="18" viewBox="0 0 24 24" style="margin-top:4px"><path fill="#fff" d="M6.6 10.8c1.4 2.8 3.8 5.1 6.6 6.6l2.2-2.2c.3-.3.7-.4 1-.2 1.1.4 2.3.6 3.6.6.6 0 1 .4 1 1V20c0 .6-.4 1-1 1C10.6 21 3 13.4 3 4c0-.6.4-1 1-1h3.5c.6 0 1 .4 1 1 0 1.3.2 2.5.6 3.6.1.3 0 .7-.2 1z"/></svg><span>(555) 014-2290.</span></div>
  <div style="margin-top:4px"><svg width="20" height="14" viewBox="0 0 20 14" style="margin-top:8px"><rect x="1" y="1" width="18" height="12" fill="none" stroke="#fff" stroke-width="1.6"/><path d="M1 1l9 7 9-7" fill="none" stroke="#fff" stroke-width="1.6"/></svg><span>hello@meridanehaulage.com</span></div>
</div>
<h3 class="abs" style="left:889px;top:2945px;font-family:'Roboto',sans-serif;font-size:20px;color:#fff">Newsletter</h3>
<p class="abs foot-text" style="left:889px;top:3015px;width:260px;color:#fff">Register your email for News for Meridane Haulage</p>
<div class="abs field" style="left:889px;top:3086px;width:221px;height:35px;padding:8px 10px;font-size:12px">Enter the email</div>
<div class="abs btn btn-ghost" style="left:887px;top:3145px;width:127px;height:37px;font-size:16px">Send</div>
<p class="abs" style="left:92px;top:3238px;font-size:15px;color:#fff">Copyright © 2019 Meridane Haulage All Rights Reserved.</p>
<div class="abs social" style="left:966px;top:3239px"><span></span><span></span><span></span><span></span><span></span></div>
</body>
</html>
```